Ridge Slogan Copy and Design

Create a slogan for Ridge Pro a boxing, kick boxing, gym fitness equipment and clothing brand. We would like different versions (in terms of fonts and colours) of some of the slogans in the attached word document.

Updates
12 May 2:19PM - We have refined the slogans to use and don''t want you to come up with new slogans. We would like some slogans from the word file and submit them in different colours and fonts.

Themes
Tough
Professional
Quality
Updates

Target Market(s)

Requirements
Must have
• Multiple versions of the slogan - in terms of font and colourĀ 

Nice to have
• A version where the font is bold and solid suitable for use with a logo like thisĀ

```html
<!DOCTYPE html>
<html lang="en">
<head>
<meta charset="utf-8">
<title>Ridge Pro Slogans</title>
<link rel="stylesheet" href="https://fonts.googleapis.com/css2?family=Roboto+Condensed:ital,wght@0,700;1,700&display=swap">
<style>
  :root {
    --lime: #c2ff0a;
    --green: #6cbd0b;
    --ink: #0d0d0d;
    --paper: #ffffff;
  }
  html, body {
    margin: 0;
    padding: 0;
    width: 1200px;
    height: 982px;
    overflow: hidden;
    background: var(--paper);
  }
  .slogan-sheet {
    display: block;
    width: 1200px;
    height: 982px;
  }
  .slogan {
    font-family: "Roboto Condensed", "Arial Narrow", sans-serif;
    font-weight: 700;
    font-size: 76px;
    letter-spacing: -1px;
    fill: var(--lime);
  }
  .slogan .accent { font-style: italic; }
  .slogan .strong { fill: var(--green); }
  .slogan--ink { fill: var(--ink); }
</style>
</head>
<body>
<svg class="slogan-sheet" viewBox="0 0 1200 982" xmlns="http://www.w3.org/2000/svg" aria-label="Ridge Pro slogans">
  <text class="slogan" x="56" y="139">vengeance is a <tspan class="accent">virtue</tspan></text>
  <text class="slogan" x="56" y="236">champions prevail</text>
  <text class="slogan slogan--ink" x="56" y="333">never back down</text>
  <text class="slogan" x="56" y="430">by <tspan class="strong">professionals</tspan> for <tspan class="strong">professionals</tspan></text>
  <text class="slogan" x="56" y="528">fight wear</text>
  <text class="slogan" x="56" y="625">ridge professional fighter</text>
  <text class="slogan" x="56" y="723"><tspan class="accent">by</tspan> fighters <tspan class="accent">for</tspan> fighters</text>
  <text class="slogan" x="62" y="826"><tspan class="strong">total</tspan></text>
  <text class="slogan" x="62" y="900">domination</text>
</svg>
</body>
</html>
```